Visitenkarten-Design für Immobilienmakler
Zielgruppe
Immobilienmakler
Aufgabenstellung
Top moderne hochwertige Visitenkate, wir hätten gerne eine sehr hochwertig moderne Visitenkarte mit Bild vom Mitarbeiter... Anbei habe ich die alte Visitenkarte die ich sehr kindlich finde... Es sollte jetzt sehr exklusive aussehen. Alle Daten können von der alten Visitenkarte übernommen werden.. danke

```html
<!DOCTYPE html>
<html lang="de">
<head>
<meta charset="utf-8">
<title>Velmar Agentur – Visitenkarte</title>
<link rel="stylesheet" href="https://fonts.googleapis.com/css2?family=PT+Sans:wght@400;700&display=swap">
<style>
  :root {
    --page: #ffffff;
    --card-light: #ffffff;
    --card-dark: #000000;
    --green: #1b8a3b;
    --ink: #111111;
    --grey: #8a8a8a;
    --ring: #eef0ea;
    --photo-a: #e4e4e4;
    --photo-b: #8c8c8c;
  }
  * { margin: 0; padding: 0; box-sizing: border-box; }
  html, body { width: 1200px; height: 1200px; overflow: hidden; background: var(--page); }
  body { position: relative; font-family: "PT Sans", sans-serif; }

  .card {
    position: absolute;
    left: 296px;
    width: 582px;
    height: 376px;
    overflow: hidden;
    box-shadow: 4px 5px 8px rgba(0,0,0,0.35);
  }
  .card--front { top: 192px; background: var(--card-light); border: 1px solid #c9c9c9; }
  .card--back { top: 647px; background: var(--card-dark); }

  .brand {
    position: absolute;
    right: 36px;
    top: 30px;
    text-align: right;
  }
  .brand__name {
    display: block;
    font-weight: 700;
    font-size: 45px;
    line-height: 1;
    letter-spacing: -0.5px;
    color: var(--green);
  }
  .brand__tagline {
    display: block;
    margin-top: 14px;
    margin-right: 14px;
    font-size: 13px;
    letter-spacing: 1.2px;
    text-transform: uppercase;
    color: var(--ink);
  }
  .card--back .brand__name,
  .card--back .brand__tagline { color: #ffffff; }

  .portrait {
    position: absolute;
    left: -16px;
    top: 80px;
    width: 106px;
    height: 106px;
  }

  .person {
    position: absolute;
    left: 80px;
    top: 183px;
  }
  .person__name {
    font-weight: 700;
    font-size: 20px;
    line-height: 24px;
    color: var(--ink);
  }
  .person__role {
    font-size: 16.5px;
    line-height: 20px;
    color: var(--grey);
  }
  .contact {
    margin-top: 10px;
    list-style: none;
    font-size: 16.5px;
    line-height: 19.5px;
    color: var(--green);
  }
</style>
</head>
<body>
  <section class="card card--front">
    <div class="brand">
      <span class="brand__name">Velmar Agentur</span>
      <span class="brand__tagline">Der Immobilienmakler</span>
    </div>

    <svg class="portrait" viewBox="0 0 106 106" role="img" aria-label="Porträtfoto des Mitarbeiters in Schwarzweiß">
      <defs>
        <linearGradient id="photoTone" x1="0" y1="0" x2="0" y2="1">
          <stop offset="0" stop-color="var(--photo-a)"/>
          <stop offset="1" stop-color="var(--photo-b)"/>
        </linearGradient>
      </defs>
      <circle cx="53" cy="53" r="49" fill="#ffffff" stroke="var(--ring)" stroke-width="7"/>
      <circle cx="53" cy="53" r="42" fill="url(#photoTone)"/>
    </svg>

    <div class="person">
      <p class="person__name">Lukas Berger</p>
      <p class="person__role">Dipl. Immobilienmanager</p>
      <p class="person__role">Geschäftsführer</p>
      <ul class="contact">
        <li>Am Feldweg 12 · 6850 Dornbirn</li>
        <li>Tel. +43 5572 40 218-14 · Mobil +43 660 4817 296</li>
        <li>Mail: lukas@velmar-agentur.com</li>
        <li>Web: www.velmar-agentur.com</li>
      </ul>
    </div>
  </section>

  <section class="card card--back">
    <div class="brand">
      <span class="brand__name">Velmar Agentur</span>
      <span class="brand__tagline">Der Immobilienmakler</span>
    </div>
  </section>
</body>
</html>
```